Book cover for "Steady Broker" focused on scaling up an Insurance Agency

Front Cover:
We need book cover for our upcoming book with title "Steady Broker" . Subtitle of book is "The secrets behind building a multi-million dollar Insurance agency:Interviews, success stories and framework for success".
On top line it should say " Foreword by Mark Holloway".
Author name : "Ravindra Kulkarni"
This book will help insurance agents in scaling up their agency. It will also help someone looking to start a business or side hustle.

Back Cover:
It should contain content provided below and image of author attached.
"
Who should read this book?

Do you know that starting an Insurance Agency is probably one of the best business ideas?
Do you want to know how some startups created billion dollar plus insurance based companies in the last 5-10 years?
Do you want to know the secrets behind building a multi-million dollar Insurance agency?
Do you want to know how to scale up an Insurance Agency profitably?
Do you want to know how to cut through the noise in the market and differentiate your business?
How to leverage technology to rise above (be seen and heard) the myriad of agencies around you and compete with both local and online agencies?
How to build a team which carries your mindset to take care of clients and grow your business?
(above list should be bulleted)
If you are interested in learning about these topics then you are at the right place.

You can either spend years figuring out things yourself or read this book and get wisdom from successful agents and thought leaders at top insurance agencies."

Spine:
" Steady Broker by Ravindra Kulkarni"

Requirements:
One file should be only book cover.
Other file should contain :front cover, back cover and spine as one file.
It should follow standard for Norvel PBX, link provided below.
https://pbx.norvelbooks.example/en_US/help/topic/Q774210385

Target Market(s)

Insurance Agents
People looking to start a new business
Side Hustlers

Industry/Entity Type

Insurance Agency

Font styles to use
Serif

```html
<!DOCTYPE html>
<html lang="en">
<head>
<meta charset="utf-8">
<title>Steady Broker — Front Cover</title>
<link href="https://fonts.googleapis.com/css2?family=Libre+Caslon+Text:ital,wght@0,400;0,700;1,400&display=swap" rel="stylesheet">
<style>
  :root {
    --page-bg: #ffffff;
    --cover-black: #07090d;
    --suit-navy: #1b2433;
    --suit-mid: #2c3648;
    --gold: #c9ad72;
    --gold-light: #eadbb0;
    --gold-deep: #a8874c;
    --ink-white: #f2f0ea;
    --band-ink: #141414;
  }
  * { box-sizing: border-box; margin: 0; padding: 0; }
  html, body {
    width: 1200px; height: 960px; overflow: hidden;
    background: var(--page-bg);
  }
  body { position: relative; font-family: "Libre Caslon Text", "Times New Roman", serif; }

  .book-cover {
    position: absolute; left: 305px; top: 40px;
    width: 590px; height: 880px;
    background: var(--cover-black);
    overflow: hidden;
  }
  .cover-photo {
    position: absolute; left: 0; top: 0; width: 100%; height: 620px;
    background:
      radial-gradient(ellipse 30% 45% at 50% 8%, #c9ccd2 0%, rgba(201,204,210,0) 60%),
      radial-gradient(ellipse 70% 60% at 50% 40%, var(--suit-mid) 0%, var(--suit-navy) 55%, rgba(7,9,13,0) 100%),
      linear-gradient(180deg, var(--suit-navy) 0%, #141b27 65%, var(--cover-black) 100%);
  }
  .foreword {
    position: absolute; top: 62px; left: 0; width: 100%;
    text-align: center; color: var(--ink-white);
    font-size: 19px; letter-spacing: 0.2px;
  }
  .title {
    position: absolute; top: 268px; left: 0; width: 100%;
    text-align: center; color: var(--gold);
    font-weight: 400; font-size: 44px; line-height: 56px;
    letter-spacing: 7px;
  }
  .subtitle {
    position: absolute; top: 522px; left: 50%; transform: translateX(-50%);
    width: 310px; list-style: none;
  }
  .subtitle li {
    border: 1px solid var(--gold-deep);
    color: var(--ink-white);
    text-align: center; text-transform: uppercase;
    font-size: 17px; letter-spacing: 1.4px;
    height: 33px; line-height: 32px;
    margin-bottom: 3px;
  }
  .tagline {
    position: absolute; top: 690px; left: 0; width: 100%;
    text-align: center; color: var(--ink-white);
    font-style: italic; font-size: 17px; line-height: 25px;
  }
  .author-band {
    position: absolute; left: 0; bottom: 0; width: 100%; height: 128px;
    background: linear-gradient(90deg, var(--gold-deep) 0%, var(--gold-light) 45%, var(--gold) 70%, var(--gold-deep) 100%);
    display: flex; align-items: center; justify-content: center;
  }
  .author {
    color: var(--band-ink); font-weight: 700;
    font-size: 32px; letter-spacing: 6px; text-transform: uppercase;
    white-space: nowrap;
  }
</style>
</head>
<body>
  <main class="book-cover">
    <div class="cover-photo" role="img" aria-label="Photograph of a businessman in a dark suit and tie, hands cupped protectively one above the other"></div>
    <p class="foreword">Foreword by Mark Holloway</p>
    <h1 class="title">STEADY<br>BROKER</h1>
    <ul class="subtitle">
      <li>The Secrets</li>
      <li>Behind Building A</li>
      <li>Multi-Million Dollar</li>
      <li>Insurance Agency</li>
    </ul>
    <p class="tagline">Interviews, success stories<br>and framework for success</p>
    <div class="author-band">
      <p class="author">Ravindra Kulkarni</p>
    </div>
  </main>
</body>
</html>
```